Law Office needs stationery design and business card

I currently have been using the same letterhead for the last 8 years. Since i 'm about to adding another location, I want to revamp my letterhead and business card. I already have a logo i'm happy with. I will upload my current letterhead, fax sheet, envelope, and logos. I need a business card also. I have 2 locations, 1 phone number, 1 fax line, website, etc. If possible and fitting with the design, I would like to keep the same information listed currently on the letterhead.

**Keep in mind, I also NEED A FAX SHEET COVER. thank you
Updates

Hello, Please submit a Gray Scale or Black and White version of your designs also, since most of the time I will be printing NON color stationery. I will seldom use a color print for my letterhead, I would like to have a color version for my benefit, however i will print in grayscale majority of the time . For the Business Card, that can just be in color. When I get my business cards they will be in color.Thank youEnrique Added Sunday, September 18, 2016

Industry/Entity Type

Business

```html
<!DOCTYPE html>
<html lang="en">
<head>
<meta charset="utf-8">
<title>Harrow Law Stationery</title>
<link href="https://fonts.googleapis.com/css2?family=Arimo:ital,wght@0,400;0,700;1,400&family=Source+Sans+3:wght@400;600&display=swap" rel="stylesheet">
<style>
:root{
  --backdrop:#a9a7a8;
  --paper:#f6f5f3;
  --gold:#c2a261;
  --ink:#1d1b1a;
  --text:#3e3c3a;
  --field:#e8e8e8;
}
*{margin:0;padding:0;box-sizing:border-box}
html,body{width:1200px;height:1120px;overflow:hidden;background:var(--backdrop)}
body{position:relative;font-family:"Arimo",sans-serif;color:var(--text)}
.sheet{position:absolute;background:var(--paper);transform-origin:0 0;transform:scale(.858);box-shadow:0 3px 10px rgba(0,0,0,.25)}
.sheet.full{width:637px;height:898px}
.sheet.short{width:637px;height:289px}
.letter{left:45px;top:36px}
.fax{left:611px;top:36px}
.label-sheet{left:45px;top:826px}
.envelope{left:614px;top:826px;width:636px;height:289px}
.edge{position:absolute;left:0;right:0;bottom:0;height:12px;border-top:2px solid var(--ink);background:var(--gold);box-shadow:inset 0 2px 0 var(--paper)}
.brand{position:absolute;display:flex;flex-direction:column;align-items:center;gap:8px}
.brand-mark{width:40px;height:40px;background:var(--gold);transform:rotate(45deg)}
.brand-name{font-family:"Arimo",sans-serif;font-weight:400;font-size:19px;letter-spacing:1.5px;color:var(--ink)}
.letter .brand,.fax .brand{left:62px;top:42px}
.attorneys{position:absolute;top:58px;left:230px;display:flex;font-size:11px;line-height:14.5px}
.attorneys .col{padding:0 13px}
.attorneys .col.left{text-align:right;border-right:1px solid var(--ink);width:195px}
.attorneys .name{color:var(--gold)}
.attorneys .mail{font-style:italic;color:var(--ink);margin-bottom:3px}
.salutation{position:absolute;left:63px;top:252px;font-family:"Source Sans 3",sans-serif;font-size:17px;color:var(--text)}
.body-copy{position:absolute;left:63px;top:304px;width:516px;font-family:"Source Sans 3",sans-serif;font-size:9.6px;line-height:15.3px;color:var(--text);text-align:justify}
.body-copy p{margin-bottom:15.3px}
.closing{position:absolute;left:63px;top:627px;font-family:"Source Sans 3",sans-serif;font-size:10px;color:var(--text)}
.signature{position:absolute;left:60px;top:646px;width:86px;height:38px;background:linear-gradient(90deg,#e6e5e3,#d4d4d6)}
.signer{position:absolute;left:67px;top:694px;font-family:"Source Sans 3",sans-serif;font-size:10.5px;line-height:17px}
.footer{position:absolute;left:62px;width:514px;top:826px;font-size:10px;color:var(--text)}
.footer .row{display:flex;justify-content:center;align-items:center;gap:6px;white-space:nowrap}
.footer .row.top{padding-bottom:5px;border-bottom:1px solid #777}
.footer .row.bottom{padding-top:6px;gap:5px}
.ico{width:9px;height:10px;fill:var(--gold);flex:none}
.fb{width:8px;height:8px;background:var(--gold);display:inline-block;flex:none}
.fax-table{position:absolute;left:36px;top:192px;width:564px;display:grid;grid-template-columns:75px 200px 76px 200px;gap:3px 4px}
.fax-table div{background:var(--field);height:27px;font-size:11px;color:var(--ink);padding:9px 0 0 13px}
.checks{position:absolute;left:38px;top:322px;width:560px;font-size:9px;color:var(--ink)}
.checks span{position:absolute;display:flex;align-items:center;gap:6px;white-space:nowrap}
.checks i{width:12px;height:12px;border:1px solid var(--ink);display:inline-block}
.comments{position:absolute;left:41px;top:352px;font-size:12.5px;color:var(--ink)}
.label-sheet .brand{left:28px;top:18px}
.addresses{position:absolute;left:28px;top:106px;font-size:10.5px;line-height:12px;color:var(--text)}
.addresses .addr{display:flex;gap:6px;margin-bottom:10px}
.addresses .ico{margin-top:2px}
.label-sheet .edge{height:11px}
.flap{position:absolute;left:0;top:0}
.env-brand{position:absolute;left:0;right:0;top:20px;display:flex;flex-direction:column;align-items:center;gap:10px}
.env-brand .mark{width:34px;height:34px;background:var(--paper);transform:rotate(45deg)}
.env-brand .name{font-size:17px;letter-spacing:1.5px;color:var(--paper)}
.env-brand .url{font-size:10px;color:var(--paper)}
</style>
</head>
<body>

<svg width="0" height="0" style="position:absolute">
  <defs>
    <symbol id="pin" viewBox="0 0 10 12"><path d="M5 0a4 4 0 0 1 4 4c0 3-4 8-4 8S1 7 1 4a4 4 0 0 1 4-4zm0 2.3a1.7 1.7 0 1 0 0 3.4 1.7 1.7 0 0 0 0-3.4z"/></symbol>
    <symbol id="phone" viewBox="0 0 12 10"><path d="M0 3c2-3 10-3 12 0v2H9V3.5H3V5H0zM2 5h8l1 5H1z"/></symbol>
    <symbol id="mobile" viewBox="0 0 8 12"><path d="M1 0h6a1 1 0 0 1 1 1v10a1 1 0 0 1-1 1H1a1 1 0 0 1-1-1V1a1 1 0 0 1 1-1zm.5 1.5v8h5v-8z"/></symbol>
    <symbol id="mail" viewBox="0 0 12 9"><path d="M0 0h12L6 5zM0 1.5l6 4.5 6-4.5V9H0z"/></symbol>
    <symbol id="globe" viewBox="0 0 12 12"><circle cx="6" cy="6" r="6"/></symbol>
  </defs>
</svg>

<!-- Letterhead -->
<section class="sheet full letter">
  <div class="brand"><span class="brand-mark"></span><span class="brand-name">HARROW LAW</span></div>
  <div class="attorneys">
    <div class="col left">
      <div class="name">Tobias Marlowe Esq.</div><div class="mail">Tobias@HarrowLaw.com</div>
      <div class="name">Nora Kessling Esq.</div><div class="mail">Nora@HarrowLaw.com</div>
    </div>
    <div class="col">
      <div class="name">Claire Dunn Esq.</div><div class="mail">Claire@HarrowLaw.com</div>
      <div class="name">Grant Ellis Esq. of counsel</div><div class="mail">Grant@HarrowLaw.com</div>
    </div>
  </div>
  <div class="salutation">Dear Mr. Smith,</div>
  <div class="body-copy">
    <p>Lorem ipsum dolor sit amet, consectetur adipiscing elit. Donec orci purus, luctus vitae dignissim eu, iaculis sed purus. Vivamus faucibus, ipsum nec aliquet viverra, leo mauris condimentum ligula, sit amet sagittis enim ligula quis arcu. Nam egestas tortor id nisi porttitor mattis. In tortor ante, ultricies in suscipit a, tempus non massa. Vivamus et auctor mi. Fusce vel massa nulla. Phasellus nec eros mauris, et scelerisque orci.</p>
    <p>Donec malesuada orci vitae nulla accumsan porta a id massa. Quisque accumsan iaculis magna sit amet fringilla. Maecenas consequat, magna eget tincidunt semper, odio nibh rutrum mi, id feugiat ante nisi eu risus. Vestibulum nunc orci, rhoncus a placerat in, ultricies in mi. Cras mattis varius eros, vel fringilla nisi suscipit eget. Quisque scelerisque sagittis nulla at porttitor.</p>
    <p>Sed id augue vitae urna euismod commodo aliquet a quam. Pellentesque arcu velit, cursus et malesuada ut, consequat et diam. Nullam erat sem, rhoncus id ullamcorper vitae, rhoncus et arcu. In ultricies ultricies nulla, ut rutrum nisi iaculis at. Donec eu magna a metus ornare faucibus. Fusce aliquet faucibus ultricies. Morbi semper, est id tincidunt gravida, sem arcu adipiscing lacus, ac bibendum nulla leo eu purus. Quisque nec diam sed risus consectetur a ccumsan quis quis nibh. Vestibulum id purus lorem.</p>
    <p>It is a long established fact that a reader will be distracted by the readable content of a page when looking at its layout. The point of using Lorem Ipsum is that it has a more-or-less normal distribution of letters, as opposed to using 'Content here, content here', making it look like readable English. Many desktop publishing packages</p>
  </div>
  <div class="closing">Sincerely,</div>
  <div class="signature" role="img" aria-label="Handwritten signature"></div>
  <div class="signer">John smith<br>CEO/ Founder</div>
  <div class="footer">
    <div class="row top"><svg class="ico"><use href="#pin"/></svg>48 North Elm St. Suite 200, Ashford, PA 19000 <svg class="ico"><use href="#pin"/></svg>716 Linden Ave, Brookvale, PA 19100</div>
    <div class="row bottom"><svg class="ico"><use href="#phone"/></svg>610.555.0142 <svg class="ico"><use href="#mobile"/></svg>484.555.0187 <svg class="ico"><use href="#mail"/></svg>Tobias@HarrowLaw.com <svg class="ico"><use href="#globe"/></svg>www.HarrowLaw.com <span class="fb"></span>HarrowLaw</div>
  </div>
  <div class="edge"></div>
</section>

<!-- Fax cover -->
<section class="sheet full fax">
  <div class="brand"><span class="brand-mark"></span><span class="brand-name">HARROW LAW</span></div>
  <div class="attorneys">
    <div class="col left">
      <div class="name">Tobias Marlowe Esq.</div><div class="mail">Tobias@HarrowLaw.com</div>
      <div class="name">Nora Kessling Esq.</div><div class="mail">Nora@HarrowLaw.com</div>
    </div>
    <div class="col">
      <div class="name">Claire Dunn Esq.</div><div class="mail">Claire@HarrowLaw.com</div>
      <div class="name">Grant Ellis Esq. of counsel</div><div class="mail">Grant@HarrowLaw.com</div>
    </div>
  </div>
  <div class="fax-table">
    <div>To</div><div></div><div>From</div><div></div>
    <div>Fax</div><div></div><div>Pages</div><div></div>
    <div>Phone</div><div></div><div>Attention</div><div></div>
    <div>Re</div><div></div><div>Fax</div><div></div>
  </div>
  <div class="checks">
    <span style="left:0"><i></i>Urgent</span>
    <span style="left:88px"><i></i>For Review</span>
    <span style="left:191px"><i></i>Please comment</span>
    <span style="left:330px;top:2px"><i></i>Please reply</span>
    <span style="left:456px"><i></i>Please recycle</span>
  </div>
  <div class="comments">Comments :</div>
  <div class="footer">
    <div class="row top"><svg class="ico"><use href="#pin"/></svg>48 North Elm St. Suite 200, Ashford, PA 19000 <svg class="ico"><use href="#pin"/></svg>716 Linden Ave, Brookvale, PA 19100</div>
    <div class="row bottom"><svg class="ico"><use href="#phone"/></svg>610.555.0142 <svg class="ico"><use href="#mobile"/></svg>484.555.0187 <svg class="ico"><use href="#mail"/></svg>Tobias@HarrowLaw.com <svg class="ico"><use href="#globe"/></svg>www.HarrowLaw.com <span class="fb"></span>HarrowLaw</div>
  </div>
  <div class="edge"></div>
</section>

<!-- Envelope front -->
<section class="sheet short label-sheet">
  <div class="brand"><span class="brand-mark"></span><span class="brand-name">HARROW LAW</span></div>
  <div class="addresses">
    <div class="addr"><svg class="ico"><use href="#pin"/></svg><span>48 North Elm St, Suite 200<br>Ashford, PA 19000</span></div>
    <div class="addr"><svg class="ico"><use href="#pin"/></svg><span>716 Linden Ave<br>Brookvale, PA 19100</span></div>
  </div>
  <div class="edge"></div>
</section>

<!-- Envelope back -->
<section class="sheet envelope">
  <svg class="flap" width="636" height="106" viewBox="0 0 636 106">
    <path d="M0 0H636L622 72Q614 106 580 106H56Q22 106 14 72Z" fill="var(--gold)"/>
  </svg>
  <div class="env-brand">
    <span class="mark"></span>
    <span class="name">HARROW LAW</span>
    <span class="url">www.HarrowLaw.com</span>
  </div>
</section>

</body>
</html>
```